Gift card design to reflect the theme from our overhead business sign

We need a gift card that aligns with our colors used for the sign. Since I am not sure what you're able to do with the limited space, if you think you can create a miniature version of the sign and add the words "Gift Card" to it. I'd like to see it. I have also uploaded the original logo we use as an other variable to use in place the horizontal one on the sign. That might be alright too. Give me a few options to consider.

Then for the back of the card there may be some legal requirements for the wording. I'll get back to you on that. First, let's focus on the design.

Also, i am sending the requirements for "Quorix" who will be the processor for the card. I will be doing custom cards so pay attention to page 4.

After the gift card, I will sending you the front of the store image with the sign in place, so you can come up with some ideas for a simple window design to go across all the windows.

How fast can you get back to me? Unlike the sign, I'm sort of in a time crunch.

Oh, one other thing, I want to change the pink in our current logo to the pink you used in the sign. So if you use our standard logo, please change the pink to the on you used for the sign.

```html
<!DOCTYPE html>
<html lang="en">
<head>
<meta charset="UTF-8">
<title>Sweet Crumb Bakery – Gift Card</title>
<link rel="stylesheet" href="https://fonts.googleapis.com/css2?family=Fredoka:wght@500;600;700&family=Poppins:wght@400;700&family=Yellowtail&display=swap">
<style>
  :root {
    --backdrop: #7b0744;
    --lime: #b2d44f;
    --orange: #f7902f;
    --pink: #ec3a96;
    --magenta: #a8226f;
    --white: #ffffff;
    --stripe: #101036;
  }
  * { box-sizing: border-box; margin: 0; padding: 0; }
  html, body { width: 1200px; height: 1200px; overflow: hidden; }
  body { background: var(--backdrop); position: relative; font-family: "Poppins", sans-serif; }

  .card { position: absolute; width: 666px; height: 400px; box-shadow: 0 10px 18px rgba(40, 0, 20, .45); overflow: hidden; }
  .card-front { left: 266px; top: 183px; background: var(--lime); }
  .card-back { left: 268px; top: 689px; background: var(--pink); }

  .front-frame { position: absolute; inset: 9px; border: 8px solid var(--orange); }

  .headline-gift {
    position: absolute; left: 170px; top: 22px;
    font-family: "Fredoka", sans-serif; font-weight: 700; font-size: 124px; line-height: 1;
    color: var(--magenta); letter-spacing: -3px;
    text-shadow: -3px -3px 0 var(--white);
  }
  .headline-card {
    position: absolute; left: 310px; top: 118px;
    font-family: "Yellowtail", cursive; font-size: 80px; line-height: 1;
    color: var(--magenta); transform: rotate(-12deg);
    text-shadow: -2px -2px 0 var(--white);
  }

  .stars { position: absolute; inset: 0; width: 100%; height: 100%; }
  .star { fill: var(--white); }

  .name-band {
    position: absolute; left: 41px; top: 239px; width: 589px; height: 121px;
    background: var(--pink); border: 3px solid var(--magenta);
  }
  .name-band-frame { position: absolute; inset: 5px; border: 4px solid var(--orange); }
  .brand-name {
    position: absolute; left: 0; right: 0; text-align: center;
    font-family: "Fredoka", sans-serif; font-weight: 600; color: var(--white); line-height: 1;
  }
  .name-band .brand-name { top: 22px; font-size: 50px; }
  .tagline {
    position: absolute; right: 90px; top: 78px;
    font-family: "Fredoka", sans-serif; font-weight: 600; font-size: 26px; color: var(--white); line-height: 1;
  }

  .back-frame { position: absolute; inset: 9px; border: 9px solid var(--white); }
  .card-back .brand-name { top: 58px; font-size: 50px; line-height: 1.05; }

  .contact { position: absolute; left: 58px; top: 236px; color: var(--white); }
  .contact-label { font-size: 22px; line-height: 1.1; }
  .contact-phone { font-weight: 700; font-size: 44px; line-height: 1; }

  .validity { position: absolute; right: 46px; top: 243px; text-align: right; color: var(--white); font-size: 23px; line-height: 1.35; }

  .mag-stripe { position: absolute; left: 0; right: 0; top: 323px; height: 30px; background: var(--stripe); }
</style>
</head>
<body>
  <svg width="0" height="0" style="position:absolute">
    <defs>
      <polygon id="star-shape" points="0,-10 2.9,-3.1 9.5,-3.1 4.2,1.2 5.9,8.1 0,4.2 -5.9,8.1 -4.2,1.2 -9.5,-3.1 -2.9,-3.1"/>
    </defs>
  </svg>

  <section class="card card-front" aria-label="Gift card front">
    <div class="front-frame"></div>
    <svg class="stars" viewBox="0 0 666 400" aria-hidden="true">
      <use href="#star-shape" class="star" transform="translate(467,76) scale(1.1)"/>
      <use href="#star-shape" class="star" transform="translate(533,76) scale(2)"/>
      <use href="#star-shape" class="star" transform="translate(478,119) scale(1.5)"/>
      <use href="#star-shape" class="star" transform="translate(219,165) scale(2)"/>
      <use href="#star-shape" class="star" transform="translate(286,163) scale(1.2)"/>
      <use href="#star-shape" class="star" transform="translate(273,207) scale(1.5)"/>
    </svg>
    <div class="headline-gift">Gift</div>
    <div class="headline-card">Card</div>
    <div class="name-band">
      <div class="name-band-frame"></div>
      <div class="brand-name">Sweet Crumb Bakery</div>
      <div class="tagline">fresh cakes to go</div>
    </div>
  </section>

  <section class="card card-back" aria-label="Gift card back">
    <div class="back-frame"></div>
    <svg class="stars" viewBox="0 0 666 400" aria-hidden="true">
      <use href="#star-shape" class="star" transform="translate(66,70) scale(2.1)"/>
      <use href="#star-shape" class="star" transform="translate(132,68) scale(1.2)"/>
      <use href="#star-shape" class="star" transform="translate(120,110) scale(1.5)"/>
      <use href="#star-shape" class="star" transform="translate(534,68) scale(1.2)"/>
      <use href="#star-shape" class="star" transform="translate(600,70) scale(2.1)"/>
      <use href="#star-shape" class="star" transform="translate(546,110) scale(1.5)"/>
    </svg>
    <div class="brand-name">Sweet Crumb<br>Bakery</div>
    <div class="contact">
      <div class="contact-label">Contact</div>
      <div class="contact-phone">555-208-4716</div>
    </div>
    <div class="validity">Valid till<br>31/08/2025</div>
    <div class="mag-stripe"></div>
  </section>
</body>
</html>
```